Morvath Real Estate Marketing Brochure

We are looking for a refresh/modern design to use on our marketing brochures...the blue paint brush stroke takes up a lot of space and isn't really speaking to us. Most of the material does not need to be reproduced...we are just looking for a clean template that we can use on all of our brochure pages, and then would like help on page 11 to make these pages look more professional.
Target Market(s)
Real Estate Developers, Small Businesses looking to lease space
Industry/Entity Type
Real Estate Development
Requirements
Nice to have
- Colors complementing the Morvath Logo

```html
<!DOCTYPE html>
<html lang="en">
<head>
<meta charset="utf-8">
<title>Morvath Partners – Brochure Cover Variants</title>
<link href="https://fonts.googleapis.com/css2?family=Lato:wght@400;700&display=swap" rel="stylesheet">
<style>
  :root {
    --backdrop: #6b6b6b;
    --paper: #ffffff;
    --navy: #1b2f5e;
    --navy-deep: #17325f;
    --navy-bright: #1d5d98;
    --ink-dark: #1a1a1a;
    --sky-light: #cfe3f6;
    --sky: #7fb0e0;
    --glass: #2f5f9c;
    --glass-dark: #1d3d6e;
    --leaf: #5f9a2e;
    --leaf-light: #b9d86a;
  }
  * { box-sizing: border-box; margin: 0; padding: 0; }
  html, body { width: 900px; height: 1200px; overflow: hidden; }
  body {
    background: radial-gradient(ellipse at center, #777 0%, var(--backdrop) 70%, #5a5a5a 100%);
    font-family: "Lato", Arial, sans-serif;
    position: relative;
  }
  .cover {
    position: absolute;
    left: 125px;
    width: 655px;
    height: 505px;
    box-shadow: 0 4px 14px rgba(0,0,0,0.35);
  }
  .cover--light { top: 68px; background: var(--paper); }
  .cover--dark {
    top: 622px;
    background: linear-gradient(90deg, var(--navy-deep) 0%, var(--navy-bright) 50%, var(--navy-deep) 100%);
  }
  .cover__title {
    position: absolute;
    top: 32px;
    width: 100%;
    text-align: center;
    font-size: 19px;
    font-weight: 400;
    color: var(--navy);
    white-space: nowrap;
  }
  .cover__title strong { font-weight: 700; }
  .cover--dark .cover__title { color: #fff; text-transform: lowercase; top: 29px; font-size: 22px; }
  .photo-grid {
    position: absolute;
    left: 72px;
    top: 71px;
    width: 522px;
    height: 381px;
    background: #fff;
    border: 1px solid #e4e4e4;
    box-shadow: 0 1px 4px rgba(0,0,0,0.2);
  }
  .cover--dark .photo-grid { top: 70px; }
  .photo { position: absolute; }
  .photo--tl { left: 2px; top: 2px; width: 257px; height: 181px;
    background: linear-gradient(160deg, var(--sky) 0%, var(--sky-light) 40%, #e9eef2 60%, #9aa9b6 85%, #6c7a62 100%); }
  .photo--tr { left: 262px; top: 2px; width: 258px; height: 181px;
    background: linear-gradient(110deg, #8fa3b8 0%, var(--glass-dark) 35%, #5d86b4 55%, #9fc6e8 70%, #3f7a2c 100%); }
  .photo--bl { left: 2px; top: 186px; width: 257px; height: 193px;
    background: linear-gradient(120deg, var(--glass-dark) 0%, var(--glass) 40%, #e8eef5 65%, #8ab4df 100%); }
  .photo--br { left: 262px; top: 186px; width: 258px; height: 193px;
    background: linear-gradient(100deg, #6f8fad 0%, #c7d9e8 30%, var(--leaf-light) 55%, var(--leaf) 80%, #2f5a1a 100%); }
  .brand-plate {
    position: absolute;
    left: 140px;
    top: 151px;
    width: 269px;
    height: 86px;
    background: linear-gradient(90deg, var(--navy-deep) 0%, #1f4f88 60%, var(--navy-bright) 100%);
    border: 2px solid #fff;
    display: flex;
    align-items: center;
    justify-content: center;
    gap: 14px;
  }
  .brand-plate__mark { width: 26px; height: 26px; background: #fff; }
  .brand-plate__text {
    display: flex;
    flex-direction: column;
    align-items: flex-end;
    color: #fff;
    line-height: 1;
  }
  .brand-plate__name {
    font-size: 34px;
    font-weight: 400;
    letter-spacing: 1px;
  }
  .brand-plate__sub {
    margin-top: 4px;
    font-size: 10px;
    font-weight: 400;
    letter-spacing: 1.5px;
  }
  .cover__url {
    position: absolute;
    bottom: 19px;
    width: 100%;
    text-align: center;
    font-size: 15px;
    letter-spacing: 2px;
    color: var(--ink-dark);
  }
  .cover--dark .cover__url { color: #fff; bottom: 19px; }
</style>
</head>
<body>
  <section class="cover cover--light">
    <h1 class="cover__title"><strong>REAL ESTATE</strong> DEVELOPMENT COMPANY</h1>
    <div class="photo-grid">
      <div class="photo photo--tl" role="img" aria-label="Modern glass office building against blue sky"></div>
      <div class="photo photo--tr" role="img" aria-label="Glass office buildings along a tree-lined walkway"></div>
      <div class="photo photo--bl" role="img" aria-label="Upward view of glass towers with sun flare"></div>
      <div class="photo photo--br" role="img" aria-label="Glass facade beside sunlit green trees"></div>
      <div class="brand-plate">
        <span class="brand-plate__mark"></span>
        <span class="brand-plate__text">
          <span class="brand-plate__name">MORVATH</span>
          <span class="brand-plate__sub">PARTNERS</span>
        </span>
      </div>
    </div>
    <p class="cover__url">www.morvathpartners.com</p>
  </section>

  <section class="cover cover--dark">
    <h1 class="cover__title"><strong>real estate</strong> development company</h1>
    <div class="photo-grid">
      <div class="photo photo--tl" role="img" aria-label="Modern glass office building against blue sky"></div>
      <div class="photo photo--tr" role="img" aria-label="Glass office buildings along a tree-lined walkway"></div>
      <div class="photo photo--bl" role="img" aria-label="Upward view of glass towers with sun flare"></div>
      <div class="photo photo--br" role="img" aria-label="Glass facade beside sunlit green trees"></div>
      <div class="brand-plate">
        <span class="brand-plate__mark"></span>
        <span class="brand-plate__text">
          <span class="brand-plate__name">MORVATH</span>
          <span class="brand-plate__sub">PARTNERS</span>
        </span>
      </div>
    </div>
    <p class="cover__url">www.morvathpartners.com</p>
  </section>
</body>
</html>
```